VORTIQ Business Card Design

We need a business card for a new company based on the Gold Coast, we are a new supplement distributing company called VORTIQ Sports Nutrition - Bold Horizon Sports Nutrition. We are providing new science based bodybuilding and fitness supplementation. Our company has a key focus towards next generation. We are wanting a card that is cool, innovative and fresh. We would like to see the implementation of the below image in a fresh and very innovative design that stands out. The final design should communicate New, Innovative, Cool, Science and researched based.
Target Market(s)
The target market is fitness and bodybuilder enthusiasts. Young audience so very cool looking.
Industry/Entity Type
Fitness
Contact Information for Business Card
(front of card)
VORTIQ Sports Nutrition.
Milo Harrow
CEO/Sport Nutrition Specialist
0473 628 904
Milo@vortiqfuelworks.example
www.vortiqfuelworks.example
(back of card)
Scientifically formulated supplement range
Private Nutrition consultations
comprehensive sports nutrition seminars
Requirements
Nice to have
- The card could have a cut out on one of the sides or one of the corners rounded off so the card looks different from a normal business card.
Should not have
- The colours need to complement each other and pop out.

```html
<!DOCTYPE html>
<html lang="en">
<head>
<meta charset="utf-8">
<title>VORTIQ Sports Nutrition – Business Card</title>
<link rel="stylesheet" href="https://fonts.googleapis.com/css2?family=Open+Sans:ital,wght@0,300;0,400;0,600;0,700;1,400&display=swap">
<style>
  :root {
    --page-bg: #ffffff;
    --navy-top: #123243;
    --navy-mid: #0f1f28;
    --ink-black: #07090b;
    --sky: #6dcff6;
    --paper: #ffffff;
    --text-dark: #3d3d3d;
    --text-mid: #555555;
  }
  * { margin: 0; padding: 0; box-sizing: border-box; }
  html, body {
    width: 1200px; height: 1000px; overflow: hidden;
    background: var(--page-bg);
    font-family: "Open Sans", Arial, sans-serif;
  }
  .canvas { position: relative; width: 1200px; height: 1000px; }

  .card {
    position: absolute; left: 322px; width: 555px; height: 343px;
    overflow: hidden;
    background: linear-gradient(180deg, var(--navy-top) 0%, var(--navy-mid) 45%, var(--ink-black) 100%);
    filter: drop-shadow(4px 6px 6px rgba(0,0,0,0.25));
  }
  .card--front { top: 135px; border-radius: 0 45px 0 45px; }
  .card--back  { top: 516px; border-radius: 45px 0 45px 0; }
  .card svg.shapes { position: absolute; inset: 0; }

  .brand-name {
    position: absolute; left: 66px; top: 180px; width: 176px;
    text-align: center;
    font-weight: 700; font-size: 44px; letter-spacing: 1px;
    color: var(--sky); line-height: 1;
  }
  .tagline {
    position: absolute; left: 33px; top: 268px;
    font-style: italic; font-size: 12.5px; color: var(--paper);
    letter-spacing: 0.2px;
  }

  .contact {
    position: absolute; right: 27px; top: 104px; width: 240px;
    text-align: right; color: var(--text-dark);
  }
  .contact__name {
    font-weight: 300; font-size: 37px; line-height: 1; letter-spacing: 0.5px;
    color: var(--text-dark);
    padding-bottom: 6px; border-bottom: 2px solid var(--sky);
  }
  .contact__role {
    font-weight: 700; font-size: 12.5px; line-height: 1;
    padding: 6px 0 5px; border-bottom: 2px solid var(--sky);
  }
  .contact__phone {
    margin-top: 10px;
    font-weight: 600; font-size: 25px; line-height: 1;
    display: flex; justify-content: flex-end; align-items: center; gap: 5px;
  }
  .contact__phone svg { width: 20px; height: 22px; }
  .contact__email { margin-top: 9px; font-size: 12.5px; color: var(--text-mid); line-height: 1.3; }
  .contact__web { font-weight: 700; font-size: 12.5px; color: var(--text-mid); line-height: 1.3; }

  .services {
    position: absolute; left: 0; right: 0; top: 110px;
    list-style: none; text-align: center;
    color: var(--paper); font-weight: 700; font-size: 16px; line-height: 29.5px;
  }
</style>
</head>
<body>
<main class="canvas">

  <section class="card card--front" aria-label="Business card front">
    <svg class="shapes" width="555" height="343" viewBox="0 0 555 343" aria-hidden="true">
      <path d="M160,0 C250,30 285,130 292,220 C298,290 330,330 380,343 L555,343 L555,0 Z" fill="var(--paper)"/>
      <path d="M145,0 C235,30 275,130 284,220 C290,290 320,330 362,343 L378,343 C334,328 302,290 296,220 C288,130 252,30 165,0 Z" fill="var(--sky)"/>
      <path d="M200,0 C330,10 460,40 555,120 L555,0 Z" fill="var(--navy-mid)"/>
      <path d="M190,0 C320,8 470,45 555,110 L555,128 C460,55 330,15 205,3 Z" fill="var(--sky)"/>
    </svg>

    <div class="brand-name">VORTIQ</div>
    <p class="tagline">BOLD HORIZON SPORTS NUTRITION.</p>

    <div class="contact">
      <h1 class="contact__name">MILO HARROW</h1>
      <p class="contact__role">CEO/SPORT NUTRITION SPECIALIST</p>
      <p class="contact__phone">
        <svg viewBox="0 0 24 24" aria-hidden="true"><path fill="var(--text-dark)" d="M6.6 2.2c.6-.4 1.4-.3 1.8.3l2.4 3.6c.4.6.3 1.4-.3 1.8L8.9 9c.9 2.4 2.8 4.8 5.1 6.3l1.2-1.5c.5-.5 1.3-.6 1.8-.2l3.5 2.6c.6.4.7 1.2.3 1.8l-1.6 2.2c-.7.9-1.9 1.3-3 .9C9.4 18.8 4.7 13.3 3.4 6.4c-.2-1.1.3-2.2 1.2-2.8z"/></svg>
        0473 628 904
      </p>
      <p class="contact__email">Milo@vortiqfuelworks.example</p>
      <p class="contact__web">www.vortiqfuelworks.example</p>
    </div>
  </section>

  <section class="card card--back" aria-label="Business card back">
    <svg class="shapes" width="555" height="343" viewBox="0 0 555 343" aria-hidden="true">
      <path d="M0,165 C110,30 300,0 555,165 L555,177 C300,20 120,40 0,180 Z" fill="var(--sky)"/>
      <path d="M0,180 C120,40 300,20 555,177 L555,181 C300,28 125,48 0,198 Z" fill="var(--paper)"/>
      <path d="M0,262 C130,292 270,285 380,252 C450,232 510,236 555,258 L555,268 C510,248 455,246 385,266 C270,300 130,302 0,270 Z" fill="var(--sky)"/>
      <path d="M0,260 C130,288 270,280 380,248 C450,228 510,232 555,252 L555,258 C510,238 450,234 380,254 C270,286 130,294 0,264 Z" fill="var(--paper)"/>
    </svg>

    <ul class="services">
      <li>SCIENTIFICALLY FORMULATED</li>
      <li>SUPPLEMENT RANGE</li>
      <li>PRIVATE NUTRITION CONSULTATIONS</li>
      <li>COMPREHENSIVE SPORTS NUTRITION SEMINARS</li>
    </ul>
  </section>

</main>
</body>
</html>
```